Larkspur Ridge Management - Business Cards

I need business cards. My current logo was designed by a designer at this site and I very much like and am happy with the results. I would like a business card that is trendy, unique, current yet professional. I deal with high net worth clients daily

Target Market(s)

Out of state investors looking to get into the rental market in Ohio

Industry/Entity Type

Property Management, Consulting

Contact Information for Business Card

Name, Title (Chief Financial Officer) office phone number (555) 817-3094 website address larkridgemgmt.example

Font styles to use
Sans Serif

Colors
0054AA
0677BA
7BADD7
CADEEF
E8F1F8
0094D4
00A9DD
6FCCEA
C7EBF8
E9F6FB
00AB8E
00BBA5
67D7C9
C6EFE9
E9F9F6

```html
<!DOCTYPE html>
<html lang="en">
<head>
<meta charset="utf-8">
<title>Larkspur Ridge Management – Business Cards</title>
<link rel="stylesheet" href="https://fonts.googleapis.com/css2?family=Montserrat:wght@500;600;700;800&display=swap">
<style>
  :root {
    --navy: #1e3a6e;
    --blue-top: #2c5fab;
    --blue-bottom: #1c3d78;
    --red: #d8262e;
    --white: #ffffff;
    --ink: #2b2f3a;
    --page: #ffffff;
  }
  * { box-sizing: border-box; margin: 0; padding: 0; }
  html, body {
    width: 1200px; height: 1200px; overflow: hidden;
    background: var(--page);
    font-family: "Montserrat", Arial, sans-serif;
  }
  .stage { position: relative; width: 1200px; height: 1200px; }

  .card {
    position: absolute;
    width: 448px; height: 262px;
    overflow: hidden;
    box-shadow: 10px 12px 14px rgba(0,0,0,0.35);
  }
  .card-front { left: 110px; top: 469px; }
  .card-back  { left: 669px; top: 473px; height: 258px; background: var(--white); }

  /* front */
  .front-field {
    position: absolute; inset: 0;
    background: linear-gradient(180deg, var(--blue-top) 0%, #244f96 45%, var(--blue-bottom) 100%);
  }
  .front-name {
    position: absolute; left: 0; right: 0; top: 86px;
    text-align: center; color: var(--white);
    font-weight: 800; font-size: 26px; line-height: 1.2;
    letter-spacing: 0.5px; text-transform: uppercase;
  }
  .band { position: absolute; left: 0; bottom: 0; width: 100%; height: 40px; }
  .web-label {
    position: absolute; bottom: 0;
    display: flex; align-items: center; justify-content: center; gap: 6px;
    color: var(--white); font-weight: 700; letter-spacing: 0.2px;
    white-space: nowrap;
  }
  .card-front .web-label { left: 112px; width: 232px; height: 32px; font-size: 13.5px; }
  .card-back .web-label { left: 204px; width: 216px; height: 30px; font-size: 12.5px; }
  .globe { width: 12px; height: 12px; flex: none; }

  /* back */
  .back-brand {
    position: absolute; left: 16px; top: 20px; width: 120px;
    color: var(--navy); font-weight: 800; font-size: 13px; line-height: 1.2;
    text-transform: uppercase;
  }
  .person {
    position: absolute; right: 42px; top: 89px; text-align: right;
  }
  .person-name { color: var(--navy); font-weight: 700; font-size: 18px; }
  .person-title { color: var(--red); font-weight: 500; font-size: 12.5px; margin-top: 4px; }
  .accent-bar {
    position: absolute; right: 22px; top: 94px; width: 4px; height: 36px; background: var(--red);
  }
  .divider {
    position: absolute; left: 15px; top: 121px; width: 218px; height: 1px; background: var(--red);
  }
  .contacts {
    position: absolute; left: 15px; top: 140px; list-style: none;
    color: var(--ink); font-weight: 500; font-size: 13px;
  }
  .contacts li { display: flex; align-items: flex-start; gap: 10px; margin-bottom: 9px; line-height: 1.3; }
  .contacts svg { width: 14px; height: 14px; flex: none; margin-top: 1px; }
</style>
</head>
<body>
<main class="stage">

  <section class="card card-front" aria-label="Business card front">
    <div class="front-field" role="img" aria-label="Deep blue field with a faint repeating brand pattern"></div>
    <p class="front-name">Larkspur Ridge<br>Management</p>
    <svg class="band" viewBox="0 0 448 40" preserveAspectRatio="none" aria-hidden="true">
      <rect x="0" y="24" width="448" height="16" fill="var(--red)"/>
      <polygon points="104,40 112,8 344,8 352,40" fill="var(--navy)"/>
    </svg>
    <div class="web-label">
      <svg class="globe" viewBox="0 0 12 12" aria-hidden="true"><circle cx="6" cy="6" r="6" fill="#fff"/><path d="M1 6h10M6 1c-2 2.5-2 7.5 0 10M6 1c2 2.5 2 7.5 0 10" stroke="var(--navy)" stroke-width="1" fill="none"/></svg>
      larkridgemgmt.example
    </div>
  </section>

  <section class="card card-back" aria-label="Business card back">
    <p class="back-brand">Larkspur Ridge Management</p>

    <div class="person">
      <p class="person-name">Lorem ipsum</p>
      <p class="person-title">Chief Financial Officer</p>
    </div>
    <span class="accent-bar"></span>
    <span class="divider"></span>

    <ul class="contacts">
      <li>
        <svg viewBox="0 0 14 14" aria-hidden="true"><circle cx="7" cy="7" r="7" fill="var(--red)"/><path d="M4.5 3.6l1.3 1.6-.7.9c.5 1.1 1.3 1.9 2.4 2.4l.9-.7 1.6 1.3-.8 1.2C6.5 10.1 3.9 7.5 3.7 4.3z" fill="#fff"/></svg>
        (555) 817-3094
      </li>
      <li>
        <svg viewBox="0 0 14 14" aria-hidden="true"><circle cx="7" cy="7" r="7" fill="var(--red)"/><rect x="3.5" y="4.5" width="7" height="5" fill="#fff"/><path d="M3.5 4.7L7 7.3l3.5-2.6" stroke="var(--red)" stroke-width="0.8" fill="none"/></svg>
        ipsum@larkridgemgmt.example
      </li>
      <li>
        <svg viewBox="0 0 14 14" aria-hidden="true"><circle cx="7" cy="7" r="7" fill="var(--red)"/><path d="M7 3a2.5 2.5 0 0 1 2.5 2.5C9.5 7.5 7 10.5 7 10.5S4.5 7.5 4.5 5.5A2.5 2.5 0 0 1 7 3z" fill="#fff"/><circle cx="7" cy="5.5" r="0.9" fill="var(--red)"/></svg>
        <span>Lorem ipsum dolor sit<br>amet, consectetuer</span>
      </li>
    </ul>

    <svg class="band" viewBox="0 0 448 40" preserveAspectRatio="none" aria-hidden="true">
      <rect x="0" y="25" width="448" height="15" fill="var(--red)"/>
      <polygon points="186,40 194,8 430,8 438,40" fill="#fff"/>
      <polygon points="196,40 204,10 420,10 428,40" fill="var(--navy)"/>
    </svg>
    <div class="web-label">
      <svg class="globe" viewBox="0 0 12 12" aria-hidden="true"><circle cx="6" cy="6" r="6" fill="#fff"/><path d="M1 6h10M6 1c-2 2.5-2 7.5 0 10M6 1c2 2.5 2 7.5 0 10" stroke="var(--navy)" stroke-width="1" fill="none"/></svg>
      larkridgemgmt.example
    </div>
  </section>

</main>
</body>
</html>
```